Business Card Design and stationary (thank you cards)

I am basically starting a "handyman" business but have a little ego issue with that term. I have been a professional in the design and construction business for 30 years. I want simple…I will define the scope of work I do as i move forward, and it can vary and i want it to vary.

Target Market(s)

Homeowners mostly

Industry/Entity Type

Business

Contact Information for Business Card

Company Name is "Tidy Corner Crew" Dale P. Whitcombe, 42 Larkvale Hollow Road, Fernwick, Ma, 06419 (but I may want to use a PO Box), Phone is 860-555-0187, email is dwhitcombe584@mailnest.example,

Font styles to use
Sans Serif

Requirements
Should not have
• anything pre designed….hammers or whatever…custom lines to make home features as shone but simple and elegant

```html
<!DOCTYPE html>
<html lang="en">
<head>
<meta charset="utf-8">
<title>Tidy Corner Crew — Business Card</title>
<link href="https://fonts.googleapis.com/css2?family=Noto+Sans:wght@400;700&display=swap" rel="stylesheet">
<style>
  :root {
    --paper: #ffffff;
    --ink: #2b2b2b;
    --ink-soft: #333333;
    --rule: #6e6e6e;
    --rule-dark: #222222;
    --text: #111111;
  }
  * { margin: 0; padding: 0; box-sizing: border-box; }
  html, body {
    width: 1036px;
    height: 1200px;
    overflow: hidden;
    background: var(--paper);
  }
  .card-sheet {
    position: relative;
    width: 1036px;
    height: 1200px;
    background: var(--paper);
    font-family: "Noto Sans", Verdana, sans-serif;
  }
  .card-front {
    position: absolute;
    left: 0; top: 0;
    width: 1036px;
    height: 599px;
  }
  .company-name {
    position: absolute;
    left: 0; right: 0;
    top: 212px;
    text-align: center;
    font-size: 76px;
    font-weight: 400;
    color: var(--ink);
    letter-spacing: 2px;
    text-shadow: 2px 4px 5px rgba(0,0,0,0.25);
    white-space: nowrap;
  }
  .fold-line {
    position: absolute;
    left: 0; top: 599px;
    width: 1036px;
    height: 2px;
    background: var(--rule);
  }
  .card-back {
    position: absolute;
    left: 0; top: 601px;
    width: 1036px;
    height: 599px;
  }
  .person-name {
    position: absolute;
    left: 66px;
    top: 252px;
    font-size: 43px;
    font-weight: 700;
    color: var(--ink-soft);
    letter-spacing: 0.5px;
    text-shadow: 2px 3px 4px rgba(0,0,0,0.28);
    white-space: nowrap;
  }
  .divider {
    position: absolute;
    left: 517px;
    top: 179px;
    width: 2px;
    height: 240px;
    background: var(--rule-dark);
  }
  .contact-list {
    position: absolute;
    left: 556px;
    top: 230px;
    list-style: none;
    font-size: 19.5px;
    color: var(--text);
    line-height: 24px;
  }
  .contact-item {
    display: flex;
    align-items: flex-start;
    margin-bottom: 25px;
    white-space: nowrap;
  }
  .contact-icon {
    width: 18px;
    height: 20px;
    margin-right: 5px;
    margin-top: 2px;
    flex: none;
  }
</style>
</head>
<body>
<main class="card-sheet">
  <section class="card-front">
    <h1 class="company-name">Tidy Corner Crew</h1>
  </section>

  <div class="fold-line"></div>

  <section class="card-back">
    <h2 class="person-name">Dale P. Whitcombe</h2>
    <div class="divider"></div>
    <ul class="contact-list">
      <li class="contact-item">
        <svg class="contact-icon" viewBox="0 0 18 20" aria-hidden="true">
          <path d="M4 2 L7 2 L8 6 L6 8 Q8 12 11 14 L13 12 L16 14 L15 17 Q13 19 10 17 Q4 13 3 6 Q3 3 4 2 Z" fill="var(--text)"/>
        </svg>
        <span>860-555-0187</span>
      </li>
      <li class="contact-item">
        <svg class="contact-icon" viewBox="0 0 18 20" aria-hidden="true">
          <rect x="2" y="7" width="14" height="9" fill="var(--text)"/>
          <path d="M2.5 7.5 L9 12 L15.5 7.5" stroke="#fff" stroke-width="1.2" fill="none"/>
        </svg>
        <span>dwhitcombe584@mailnest.example</span>
      </li>
      <li class="contact-item">
        <svg class="contact-icon" viewBox="0 0 18 20" aria-hidden="true">
          <path d="M9 1 C5 1 3 4 3 7 C3 11 9 18 9 18 C9 18 15 11 15 7 C15 4 13 1 9 1 Z" fill="var(--text)"/>
          <circle cx="9" cy="7" r="2.5" fill="#fff"/>
        </svg>
        <span>42 Larkvale Hollow Road, Fernwick,<br>Ma, 06419</span>
      </li>
    </ul>
  </section>
</main>
</body>
</html>
```